4 Page Music Brochure design

We need assistance in designing a 4 Page A4 (A3 folded) Brochure promoting International Music Tour options for school groups. We have included text in the brief as well as images to be used in the brochure.

```html
<!DOCTYPE html>
<html lang="en">
<head>
<meta charset="utf-8">
<title>Skyline Group Travel – Music Tours Brochure</title>
<link href="https://fonts.googleapis.com/css2?family=Roboto:wght@300;400;700&family=Roboto+Condensed:wght@400;700&display=swap" rel="stylesheet">
<style>
:root{
  --red:#c8202b;
  --red-deep:#a5161f;
  --grey:#e6e6e6;
  --ink:#333333;
  --white:#ffffff;
  --night:#1b1512;
  --panel:#221c19;
}
*{box-sizing:border-box;margin:0;padding:0}
html,body{width:808px;height:1200px;overflow:hidden;background:#f2f2f2}
body{position:relative;font-family:"Roboto Condensed","Roboto",sans-serif;color:var(--ink)}
.spread{position:absolute;left:20px;width:768px;height:500px;overflow:hidden;background:var(--white);box-shadow:0 6px 18px rgba(0,0,0,.25)}
.spread--outer{top:45px}
.spread--inner{top:655px}
.abs{position:absolute}
.photo{position:absolute}

/* outer spread */
.intro{left:0;top:0;width:196px;height:500px;background:var(--white)}
.brand{position:absolute;display:flex;align-items:center;gap:6px;color:var(--red);font-weight:700;line-height:.9;text-transform:uppercase}
.brand__dot{width:12px;height:12px;border-radius:50%;background:var(--red);flex:none}
.intro .brand{left:20px;top:54px;font-size:22px}
.intro__box{left:0;top:100px;width:196px;height:250px;background:var(--grey);padding:22px 14px 0 22px}
.intro__lead{font-family:"Roboto",sans-serif;font-size:12.5px;line-height:1.3;color:#444;margin-bottom:14px}
.intro__body{font-size:8.6px;line-height:1.35;color:#444;margin-bottom:8px}
.partners{left:0;top:352px;width:196px;border-top:3px solid var(--red);padding:10px 0 0 22px}
.partners h3{color:var(--red);font-size:11px;font-weight:700;text-transform:uppercase;margin-bottom:10px}
.partners__grid{display:grid;grid-template-columns:repeat(4,32px);gap:10px 8px}
.partner-badge{width:32px;height:32px;border-radius:50%;background:#d9d9d9}
.partner-badge--sq{border-radius:4px}

.services{left:196px;top:0;width:192px;height:500px;background:linear-gradient(90deg,var(--red) 70%,var(--red-deep));color:var(--white);padding:56px 14px 0 14px}
.services__intro{font-size:8.5px;line-height:1.3;color:#ffd9d9}
.services h2{font-family:"Roboto",sans-serif;font-weight:300;font-size:26px;line-height:1;margin:12px 0 12px}
.services ul{list-style:none}
.services li{display:flex;gap:6px;font-size:8.2px;line-height:1.25;margin-bottom:5px}
.services li svg{flex:none;margin-top:1px}
.services__contact{position:absolute;left:14px;top:400px;font-size:11px;line-height:1.5}
.services__contact strong{font-size:11.5px;display:block}

.cover{left:388px;top:0;width:380px;height:500px}
.cover .photo{inset:0;background:linear-gradient(180deg,#ffffff 0%,#fbf3d6 18%,#f7c94a 36%,#e69a2a 48%,#6b6a74 62%,#2a3348 80%,#151b2b 100%)}
.cover .brand{left:112px;top:44px;font-size:31px;text-align:center}
.cover__mission{left:60px;top:124px;width:260px;text-align:center;font-size:9.5px;line-height:1.75;color:#222}
.cover__url{left:0;width:380px;top:446px;text-align:center;color:var(--white);font-size:15px;letter-spacing:.42em;font-family:"Roboto",sans-serif;font-weight:300}

/* inner spread */
.tour__title{font-family:"Roboto",sans-serif;font-weight:300;color:var(--white);line-height:1.1}
.tour__text{font-size:7.2px;line-height:1.4;color:#eee}
.choir-photo{left:0;top:0;width:205px;height:195px;background:linear-gradient(180deg,#d8e2ee 0%,#aebfd4 45%,#5c5e64 70%,#3e3c3a 100%)}
.choir{left:205px;top:0;width:183px;height:195px;background:var(--red);padding:34px 12px 0 14px}
.choir .tour__title{font-size:17px}
.choir__dates{font-size:9px;color:#ffe0e0;margin:6px 0 10px 12px}
.hall-photo{left:0;top:195px;width:388px;height:175px;background:linear-gradient(180deg,#1e1613 0%,#3a2a1e 50%,#6d4a26 80%,#2a1c14 100%)}
.hall{left:27px;top:208px;width:340px}
.hall .tour__title{font-size:17px;margin-bottom:4px}
.roadtrip-bg{left:0;top:370px;width:388px;height:130px;background:linear-gradient(90deg,var(--white) 55%,#d8d6d4 75%,#2a2522 100%)}
.band-photo{left:20px;top:350px;width:185px;height:128px;border:4px solid var(--white);background:linear-gradient(180deg,#6f6f78 0%,#8c2a2e 55%,#2a2a2e 100%)}
.roadtrip{left:216px;top:378px;width:160px}
.roadtrip h3{font-family:"Roboto",sans-serif;font-weight:300;color:var(--red);font-size:16px;margin-bottom:8px}
.roadtrip p{font-size:7.2px;line-height:1.4;color:#222}
.japan-photo{left:388px;top:0;width:380px;height:258px;background:linear-gradient(90deg,#5a0e0a 0%,#c2391f 30%,#e05a2a 55%,#b82a18 80%,#4a0c08 100%)}
.japan{left:417px;top:127px;width:296px;height:112px;background:rgba(28,24,22,.88);padding:14px 16px 0 18px}
.japan .tour__title{font-size:16px;text-align:center;margin-bottom:12px}
.opera-photo{left:388px;top:258px;width:191px;height:242px;background:linear-gradient(180deg,#4a2416 0%,#8c5a2a 35%,#c9a25a 55%,#3a2a22 100%)}
.european{left:579px;top:258px;width:189px;height:242px;background:var(--panel);padding:52px 14px 0 25px}
.european .tour__title{font-size:16px;margin-bottom:10px}
</style>
</head>
<body>

<section class="spread spread--outer">
  <div class="abs intro">
    <div class="brand"><span class="brand__dot"></span><span>Skyline<br>Group Travel</span></div>
    <div class="abs intro__box">
      <p class="intro__lead">Skyline Group Travel was established in 2001, to provide once in a lifetime experiences.</p>
      <p class="intro__body">Our focus is providing unique opportunities to School &amp; Sports groups that expand the horizons of students, foster personal growth, develop independence and provide memories that last a lifetime.</p>
      <p class="intro__body">Our understanding of the unique requirements of group travel and our personalised approach makes us the ideal choice in planning, sourcing and managing the perfect tour for your school or club. Our ever-growing global network allows us to offer exclusive experiences that are inaccessible to others.</p>
    </div>
    <div class="abs partners">
      <h3>Our Partners &amp; Suppliers</h3>
      <div class="partners__grid">
        <span class="partner-badge"></span><span class="partner-badge"></span><span class="partner-badge partner-badge--sq"></span><span class="partner-badge"></span>
        <span class="partner-badge"></span><span class="partner-badge partner-badge--sq"></span><span class="partner-badge partner-badge--sq"></span><span class="partner-badge partner-badge--sq"></span>
      </div>
    </div>
  </div>

  <div class="abs services">
    <p class="services__intro">Our dedicated Tour Coordinators thoroughly consult with staff to tailor an itinerary and tour management plan that meets each unique set of requirements.</p>
    <h2>We can assist in providing:</h2>
    <ul>
      <li><svg width="9" height="8" viewBox="0 0 9 8"><path d="M1 4l2.5 2.5L8 1" fill="none" stroke="#fff" stroke-width="1.8"/></svg>Customised Itineraries</li>
      <li><svg width="9" height="8" viewBox="0 0 9 8"><path d="M1 4l2.5 2.5L8 1" fill="none" stroke="#fff" stroke-width="1.8"/></svg>Negotiated Group Discounts on airfares, accommodation, transport and activities</li>
      <li><svg width="9" height="8" viewBox="0 0 9 8"><path d="M1 4l2.5 2.5L8 1" fill="none" stroke="#fff" stroke-width="1.8"/></svg>Festival/event entry</li>
      <li><svg width="9" height="8" viewBox="0 0 9 8"><path d="M1 4l2.5 2.5L8 1" fill="none" stroke="#fff" stroke-width="1.8"/></svg>Workshops with clinicians</li>
      <li><svg width="9" height="8" viewBox="0 0 9 8"><path d="M1 4l2.5 2.5L8 1" fill="none" stroke="#fff" stroke-width="1.8"/></svg>School exchanges</li>
      <li><svg width="9" height="8" viewBox="0 0 9 8"><path d="M1 4l2.5 2.5L8 1" fill="none" stroke="#fff" stroke-width="1.8"/></svg>Public performances</li>
      <li><svg width="9" height="8" viewBox="0 0 9 8"><path d="M1 4l2.5 2.5L8 1" fill="none" stroke="#fff" stroke-width="1.8"/></svg>Instrument rental</li>
      <li><svg width="9" height="8" viewBox="0 0 9 8"><path d="M1 4l2.5 2.5L8 1" fill="none" stroke="#fff" stroke-width="1.8"/></svg>Venue hire</li>
      <li><svg width="9" height="8" viewBox="0 0 9 8"><path d="M1 4l2.5 2.5L8 1" fill="none" stroke="#fff" stroke-width="1.8"/></svg>Trusted, Quality Suppliers</li>
      <li><svg width="9" height="8" viewBox="0 0 9 8"><path d="M1 4l2.5 2.5L8 1" fill="none" stroke="#fff" stroke-width="1.8"/></svg>Sightseeing</li>
      <li><svg width="9" height="8" viewBox="0 0 9 8"><path d="M1 4l2.5 2.5L8 1" fill="none" stroke="#fff" stroke-width="1.8"/></svg>Expert Guides and Tour Escorts</li>
    </ul>
    <div class="services__contact">
      <strong>Skyline Group Travel</strong>
      www.skylinegroup.travel<br>
      (02) 5550 1842<br>
      enquiry@skylinegroup.travel
    </div>
  </div>

  <div class="abs cover">
    <div class="photo" role="img" aria-label="Passenger jet parked on the airport apron at sunset, seen over the wing"></div>
    <div class="brand"><span class="brand__dot"></span><span>Skyline<br>Group Travel</span></div>
    <p class="abs cover__mission">Skyline's passion and mission remains to provide 'once in a lifetime' experiences to all of our valued customers.</p>
    <p class="abs cover__url">www.skylinegroup.travel</p>
  </div>
</section>

<section class="spread spread--inner">
  <div class="photo choir-photo" role="img" aria-label="Gothic cathedral towers against a cloudy sky"></div>
  <div class="abs choir">
    <h3 class="tour__title">Global Choir Festival</h3>
    <p class="choir__dates">(5th to the 15th of July 2020)</p>
    <p class="tour__text">Join the biggest Choral Music event in the world with Choirs from over 80 different countries and regions, taking part in adjudicated performances, individual coaching, and singing workshops. Held in Belgium in the cities Antwerp and Ghent, this is a fantastic opportunity perform on the world stage as well as take in the rich history of the Flanders region. With the option to extend your trip to include France, Germany, Italy, Austria or other nearby European Countries.</p>
  </div>

  <div class="photo hall-photo" role="img" aria-label="Concert hall facade lit up at night"></div>
  <div class="abs hall">
    <h3 class="tour__title">Liberty Concert Hall</h3>
    <p class="tour__text">The once in a life time opportunity to perform at one of the world's most famous music venues. Choirs will also have the opportunity to participate in performances, clinics, workshops, and exchanges. Based in New York City, there will also be the chance to include stops in Washington DC, Los Angeles, or San Francisco on to your trip.</p>
  </div>

  <div class="photo roadtrip-bg"></div>
  <div class="photo band-photo" role="img" aria-label="Marching band in red uniforms parading down a city street"></div>
  <div class="abs roadtrip">
    <h3>US Music Road Trip</h3>
    <p>Trace a path across the US journeying from Jazz to Blues to Soul onto Rock'n'Roll before finishing in Country Music capital of the world – Nashville. You will visit New Orleans, Memphis and Nashville where you will have the opportunity to perform at unique venues, undertake school exchanges and participate in workshops with musicians and professionals.</p>
  </div>

  <div class="photo japan-photo" role="img" aria-label="Tunnel of red shrine gates with painted lettering"></div>
  <div class="abs japan">
    <h3 class="tour__title">Japan Music Tours</h3>
    <p class="tour__text">Travel to the land of the Rising Sun and take part in school exchanges, public performances and the chance to perform at iconic theme parks Tokyo Starland and Harbour Film Park Japan. Students will have the opportunity take a Japanese Cooking Class, partake in a Traditional Japanese Tea Ceremony, see a Kabuki show, and ride the bullet train.</p>
  </div>

  <div class="photo opera-photo" role="img" aria-label="Orchestra performing on stage inside an ornate opera house"></div>
  <div class="abs european">
    <h3 class="tour__title">European<br>Instrumental<br>Tours</h3>
    <p class="tour__text">Play in Austria, France, Germany, the United Kingdom, or wherever your heart desires, you band, orchestra or ensemble will have the opportunity to perform at concert halls across Europe. As well as opportunities to participate in festivals, public performances and workshop with music professionals.</p>
  </div>
</section>

</body>
</html>
```